Build an Extreme sport website for Ridge Thrust Events Website

Platform: The website must be designed and developed using Webflow.
Pages:
Home Page:
Bold and high-impact design that reflects the extreme motorsport vibe.
Features an engaging hero section with high-quality imagery/videos.
Include sections for company highlights, key events, and sponsor logos.
Event Calendar Page:
Dynamic calendar showcasing upcoming events with dates, descriptions, and links for more details.
Sponsors Page:
Highlight our sponsors with logos, descriptions, and links to their websites.
Include a section for "How to Become a Sponsor."
Gallery/Media Page (Optional):
Showcase action-packed photos and videos from past events.
Contact Page:
Simple form for inquiries with fields for name, email, phone, and message.
Include links to social media and our physical address (if applicable).
Design Style:

Bold, trendy, and modern.
Incorporate vibrant colors and typography reflecting extreme motorsports.
High-quality visuals and media to convey energy and excitement.
Technical Features:

Fully responsive and mobile-optimized.
Easy-to-update CMS for event details, sponsor information, and media.
SEO-optimized design.
Target Audience:

Motorsports enthusiasts, sponsors, and event organizers.
References:

Use our Instagram page @ridgethrustgarage for branding inspiration.
Design should align with the high-energy, extreme motorsport aesthetic we showcase there.
Deliverables:

Fully functioning Webflow website with all pages and features outlined above.
Any graphic assets used in the design.

Target Market(s)

Side Show / Drifting / Extreme car drivers

Number of Pages Required

4 page

Font styles to use
Sans Serif

Requirements
Nice to have
• Bold, trendy, and modern. Incorporate vibrant colors and typography reflecting extreme motorsports. High-quality visuals and media to convey energy and excitement.

```html
<!DOCTYPE html>
<html lang="en">
<head>
<meta charset="utf-8">
<title>Ridge Thrust Events</title>
<link rel="stylesheet" href="https://fonts.googleapis.com/css2?family=Oswald:wght@500;600;700&family=Poppins:wght@400;500;600&display=swap">
<style>
:root{
  --red:#e0102a;
  --red-dark:#b80c1f;
  --black:#0b0b0b;
  --charcoal:#2a2a2a;
  --grey-panel:#efefef;
  --white:#ffffff;
  --text:#333333;
  --head:'Oswald',sans-serif;
  --body:'Poppins',sans-serif;
}
*{margin:0;padding:0;box-sizing:border-box}
html,body{width:1200px;height:4392px;overflow:hidden;background:var(--white)}
body{position:relative;font-family:var(--body);color:var(--text)}
a{text-decoration:none}
.abs{position:absolute}
.head{font-family:var(--head);text-transform:uppercase}

.site-header{left:0;top:0;width:1200px;height:133px;background:var(--black);z-index:3}
.brand{left:72px;top:60px;display:flex;align-items:center;gap:12px;z-index:4}
.brand-dot{width:22px;height:22px;border-radius:50%;background:var(--red);flex-shrink:0}
.brand-name{font-family:var(--head);font-weight:700;font-size:30px;color:var(--white);text-transform:uppercase;white-space:nowrap}
.call{left:802px;top:22px;display:flex;align-items:center;gap:12px;color:var(--red);font-family:var(--head);font-weight:500;font-size:27px;text-transform:uppercase;z-index:4;white-space:nowrap}
.nav{top:86px;font-family:var(--head);font-weight:600;font-size:16px;color:var(--white);text-transform:uppercase;z-index:4;white-space:nowrap}
.nav.active{color:var(--red)}

.hero{left:0;top:133px;width:1200px;height:644px;background:radial-gradient(circle at 75% 40%,#8a6a48 0%,#5a4330 35%,#2a1e15 75%,#1a130d 100%)}
.hero-title{left:124px;top:325px;font-family:var(--head);font-weight:700;font-size:94px;line-height:92px;color:var(--white);text-transform:uppercase}
.play{left:126px;top:555px;display:flex;align-items:center;gap:12px;color:var(--white);font-weight:600;font-size:21px;text-transform:uppercase}
.play-circle{width:44px;height:44px;border-radius:50%;background:var(--red);display:flex;align-items:center;justify-content:center}

.cta-text{left:271px;top:814px;font-family:var(--head);font-weight:500;font-size:26px;line-height:33px;color:#1a1a1a;text-transform:uppercase}
.btn{background:var(--red);color:var(--white);font-family:var(--head);font-weight:600;text-transform:uppercase;display:flex;align-items:center;justify-content:center}
.btn-dark{background:var(--black)}

.highlights{left:0;top:909px;width:1200px;height:688px;background:linear-gradient(160deg,#3a3a3a 0%,#1b1b1b 45%,#0e0e0e 100%)}
.section-title{width:1200px;left:0;text-align:center;font-family:var(--head);font-weight:600;text-transform:uppercase}
.card{top:1164px;width:298px;height:331px;border:4px solid var(--red);padding:9px}
.card-inner{width:100%;height:100%;border:1px solid rgba(255,255,255,.55);background:#2c2c2a;color:var(--white);text-align:center;padding:62px 22px 0}
.card.featured .card-inner{background:var(--red);border-color:rgba(255,255,255,.5)}
.card h3{font-family:var(--head);font-weight:500;font-size:20px;line-height:31px;text-transform:uppercase}
.card p{font-size:15px;line-height:26px;margin-top:26px}

.panel{left:397px;top:1722px;width:764px;height:460px;background:var(--grey-panel)}
.rule{height:2px;background:var(--red)}
.about-title{left:667px;top:1805px;font-family:var(--head);font-weight:600;font-size:54px;color:#111;text-transform:uppercase}
.about-text{left:667px;top:1892px;width:420px;font-size:15px;line-height:22px;color:#444}

.events{left:0;top:2295px;width:1200px;height:680px;background:linear-gradient(135deg,#c4091d 0%,#e0142d 50%,#b00a1c 100%)}
.event{width:488px;height:167px;background:var(--white);display:flex}
.event-thumb{width:179px;flex-shrink:0;height:100%}
.event-text{flex:1;padding:32px 20px 0 20px}
.event-text p{font-weight:500;font-size:17px;line-height:21px;color:#111}
.event-text span{display:block;margin-top:20px;font-weight:600;font-size:14px;color:var(--red)}

.sponsor-text{left:270px;top:3164px;width:660px;text-align:center;font-size:14.5px;line-height:22px;color:#444}
.sponsor{width:215px;height:106px;border:2px solid #d8d8d8;background:var(--white);display:flex;align-items:center;justify-content:center}
.sponsor-mark{width:150px;height:40px;background:#e6e6e6}

.racing{left:0;top:3598px;width:1200px;height:375px;background:linear-gradient(160deg,#2e2e2e 0%,#141414 50%,#222 100%)}
.footer{left:0;top:3973px;width:1200px;height:419px;background:linear-gradient(160deg,#333 0%,#262626 60%,#1e1e1e 100%)}
.foot-head{font-family:var(--head);font-weight:600;font-size:26px;color:var(--red);text-transform:uppercase}
.foot-list{list-style:none;font-size:15px;line-height:36px;color:#eee}
.social{width:43px;height:43px;border:2px solid #ddd;top:4114px}
.copy{left:0;top:4326px;width:1200px;text-align:center;font-size:15px;color:#ddd}
</style>
</head>
<body>

<header class="site-header abs"></header>
<div class="brand abs"><span class="brand-dot"></span><span class="brand-name">Ridge Thrust Events</span></div>
<div class="call abs">
  <svg width="22" height="22" viewBox="0 0 24 24"><path fill="#e0102a" d="M6.6 10.8a15 15 0 0 0 6.6 6.6l2.2-2.2a1 1 0 0 1 1-.25 11.4 11.4 0 0 0 3.6.57 1 1 0 0 1 1 1V20a1 1 0 0 1-1 1A17 17 0 0 1 3 4a1 1 0 0 1 1-1h3.5a1 1 0 0 1 1 1c0 1.25.2 2.45.57 3.57a1 1 0 0 1-.25 1z"/></svg>
  Call us: 123 456 7890
</div>
<nav>
  <a class="nav active abs" href="#" style="left:448px">Home</a>
  <a class="nav abs" href="#" style="left:543px">Event Calendar</a>
  <a class="nav abs" href="#" style="left:716px">Sponsors</a>
  <a class="nav abs" href="#" style="left:846px">Gallery/Media</a>
  <a class="nav abs" href="#" style="left:1011px">Contact</a>
</nav>

<section class="hero abs" role="img" aria-label="Motocross rider on a green dirt bike kicking up dust on a track"></section>
<h1 class="hero-title abs">Ridge Thrust<br>Events</h1>
<div class="play abs"><span class="play-circle"><svg width="16" height="18" viewBox="0 0 16 18"><path d="M2 1l13 8-13 8z" fill="#fff"/></svg></span>Play Now</div>

<p class="cta-text abs">Put your brand in the winners circle<br>Schedule your day at the track</p>
<a class="btn abs" href="#" style="left:750px;top:820px;width:176px;height:51px;font-size:20px">Click Here</a>

<section class="highlights abs" role="img" aria-label="Dark race track background with motion blur and checkered flag"></section>
<h2 class="section-title abs" style="top:1002px;font-size:50px;line-height:58px;color:#fff">Ridge Thrust Events<br>Company Highlights</h2>
<div class="card featured abs" style="left:128px"><div class="card-inner"><h3>Lorem ipsum dolor sit ametconsectetur</h3><p>Lorem ipsum dolor sit amt consectetur adipiscing elit sed do eiusmod temporut labore et doloren.</p></div></div>
<div class="card abs" style="left:450px"><div class="card-inner"><h3>Lorem ipsum dolor sit ametconsectetur</h3><p>Lorem ipsum dolor sit amt consectetur adipiscing elit sed do eiusmod temporut labore et doloren.</p></div></div>
<div class="card abs" style="left:772px"><div class="card-inner"><h3>Lorem ipsum dolor sit ametconsectetur</h3><p>Lorem ipsum dolor sit amt consectetur adipiscing elit sed do eiusmod temporut labore et doloren.</p></div></div>

<div class="panel abs"></div>
<div class="abs" style="left:38px;top:1722px;width:579px;height:380px;background:linear-gradient(120deg,#e7a560 0%,#8b5a3a 35%,#3a3030 70%,#1c1c1c 100%)" role="img" aria-label="Red formula race car speeding on a track at sunset"></div>
<div class="rule abs" style="left:667px;top:1773px;width:422px"></div>
<h2 class="about-title abs">About Us</h2>
<p class="about-text abs">Lorem ipsum dolor sit amet, consectetur adipiscing elit, sed do eiusmod tempor incididunt ut labore et dolore magna aliqua. Quis ipsum suspendisse ultrices gravida. Risus commodo viverra maecenas accumsan lacus vel facilisis.</p>
<a class="btn abs" href="#" style="left:667px;top:2027px;width:177px;height:53px;font-size:21px">Read More</a>
<div class="rule abs" style="left:667px;top:2125px;width:422px"></div>

<section class="events abs"></section>
<h2 class="head abs" style="left:97px;top:2384px;font-weight:600;font-size:50px;color:#fff">Our Events</h2>
<div class="abs" style="left:353px;top:2410px;width:481px;height:3px;background:#fff"></div>
<a class="btn btn-dark abs" href="#" style="left:871px;top:2382px;width:222px;height:58px;font-size:21px">Events Calendar</a>

<div class="event abs" style="left:97px;top:2486px"><div class="event-thumb" role="img" aria-label="Racer in a helmet seated in a car" style="background:linear-gradient(135deg,#6b7a88,#2b2f36)"></div><div class="event-text"><p>Lorem ipsum dolor sit amet consectetur adipiscing elitd do eiusmod tempor.</p><span>Jan 3, 2025-Jan 17, 2025</span></div></div>
<div class="event abs" style="left:607px;top:2486px"><div class="event-thumb" role="img" aria-label="Quad bike racing across sand" style="background:linear-gradient(135deg,#d9c2a8,#8a7560)"></div><div class="event-text"><p>Lorem ipsum dolor sit amet consectetur adipiscing elitd do eiusmod tempor.</p><span>Jan 3, 2025-Jan 17, 2025</span></div></div>
<div class="event abs" style="left:97px;top:2677px"><div class="event-thumb" role="img" aria-label="Motocross rider jumping in the air" style="background:linear-gradient(135deg,#c8d4de,#8c9aa6)"></div><div class="event-text"><p>Lorem ipsum dolor sit amet consectetur adipiscing elitd do eiusmod tempor.</p><span>Jan 3, 2025-Jan 17, 2025</span></div></div>
<div class="event abs" style="left:607px;top:2677px"><div class="event-thumb" role="img" aria-label="Formula cars racing on asphalt" style="background:linear-gradient(135deg,#6e6e70,#2e2e30)"></div><div class="event-text"><p>Lorem ipsum dolor sit amet consectetur adipiscing elitd do eiusmod tempor.</p><span>Jan 3, 2025-Jan 17, 2025</span></div></div>

<h2 class="section-title abs" style="top:3072px;font-size:52px;color:#111">Our Sponsors</h2>
<p class="sponsor-text abs">Lorem ipsum dolor sit amet, consectetur adipiscing elit, sed do eiusmod tempor incididunt ut labore et dolore magna aliqua. Quis ipsum suspendisse ultrices gravida. Risus commodo viverra maecenas accumsan lacus vel facilisis.</p>
<div class="sponsor abs" style="left:135px;top:3270px"><span class="sponsor-mark"></span></div>
<div class="sponsor abs" style="left:375px;top:3270px"><span class="sponsor-mark"></span></div>
<div class="sponsor abs" style="left:610px;top:3270px"><span class="sponsor-mark"></span></div>
<div class="sponsor abs" style="left:851px;top:3270px"><span class="sponsor-mark"></span></div>
<div class="sponsor abs" style="left:135px;top:3406px"><span class="sponsor-mark"></span></div>
<div class="sponsor abs" style="left:375px;top:3406px"><span class="sponsor-mark"></span></div>
<div class="sponsor abs" style="left:610px;top:3406px"><span class="sponsor-mark"></span></div>
<div class="sponsor abs" style="left:851px;top:3406px"><span class="sponsor-mark"></span></div>

<section class="racing abs" role="img" aria-label="Dark background with waving checkered flag"></section>
<h2 class="section-title abs" style="top:3703px;font-size:42px;color:#fff">Learn more about the type of racing</h2>
<a class="btn abs" href="#" style="left:307px;top:3785px;width:186px;height:61px;font-size:23px">The Cars</a>
<a class="btn abs" href="#" style="left:506px;top:3785px;width:186px;height:61px;font-size:23px">The Series</a>
<a class="btn abs" href="#" style="left:706px;top:3785px;width:189px;height:61px;font-size:23px">The Tracks</a>

<footer class="footer abs"></footer>
<div class="abs" style="left:128px;top:4118px;display:flex;align-items:center;gap:10px"><span class="brand-dot"></span><span class="brand-name" style="font-size:22px">Ridge Thrust Events</span></div>
<h4 class="foot-head abs" style="left:394px;top:4050px">Links</h4>
<ul class="foot-list abs" style="left:397px;top:4097px"><li>Home</li><li>Event Calendar</li><li>Sponsors</li><li>Gallery/Media</li><li>Contact</li></ul>
<h4 class="foot-head abs" style="left:595px;top:4050px">Contact</h4>
<ul class="foot-list abs" style="left:597px;top:4097px"><li>Ridge Thrust Events</li><li>info@company.com</li><li>Phone: 123 456 6785</li></ul>
<h4 class="foot-head abs" style="left:863px;top:4050px">Follow Us</h4>
<span class="social abs" style="left:863px" aria-label="Social link"></span>
<span class="social abs" style="left:919px" aria-label="Social link"></span>
<span class="social abs" style="left:974px" aria-label="Social link"></span>
<span class="social abs" style="left:1030px" aria-label="Social link"></span>
<div class="abs" style="left:870px;top:4186px;width:204px;height:102px;background:linear-gradient(135deg,#9a9a9a,#4a4a4a)" role="img" aria-label="Crossed checkered flags"></div>
<p class="copy abs">© 2024 Ridge Thrust Events. All Rights Reserved.</p>

</body>
</html>
```